design an extra page for our profile

we are looking for someone to create another page like the attached but with the below changes:
heading changed to (Construction)
icons changed and names to reflect new services i.e
- Residential Building
- Commercial Building
- Landscaping
- Concrete
- Painting

the very bottom of the page is to stay the same with our office info

```html
<!DOCTYPE html>
<html lang="en">
<head>
<meta charset="utf-8">
<title>Construction Services Flyer</title>
<link rel="stylesheet" href="https://fonts.googleapis.com/css2?family=Montserrat:wght@400;500;600;700&display=swap">
<style>
  :root {
    --brand-blue: #263f9c;
    --tile-blue: #1f3593;
    --ink-blue: #2a3f8f;
    --canvas-grey: #e6e6e6;
    --white: #ffffff;
    --photo-light: #eef0f4;
    --photo-mid: #c9d0dc;
  }
  * { box-sizing: border-box; margin: 0; padding: 0; }
  html, body {
    width: 1200px; height: 1000px; overflow: hidden;
    background: var(--canvas-grey);
    font-family: "Montserrat", sans-serif;
  }
  .flyer {
    position: absolute; left: 260px; top: 32px;
    width: 680px; height: 935px;
    background: var(--photo-light);
    overflow: hidden;
  }
  .backdrop-photo {
    position: absolute; left: 0; top: 170px; width: 680px; height: 682px;
    background: linear-gradient(165deg, #dfe3ea 0%, #f3f4f7 35%, #e6e9ef 60%, var(--photo-mid) 100%);
  }
  .header-photo {
    position: absolute; left: 0; top: 0; width: 680px; height: 170px;
    background: linear-gradient(90deg, #9aa6b8 0%, #c4c9d1 45%, #b33a2c 70%, #d9402f 80%, #8e959e 100%);
  }
  .header-panel { position: absolute; left: 0; top: 0; }
  .title {
    position: absolute; left: 40px; top: 52px;
    color: var(--white); font-weight: 700; font-size: 24px; letter-spacing: 0.5px;
  }
  .title-rule {
    position: absolute; left: 40px; top: 85px; width: 226px; height: 1px;
    background: var(--white);
  }
  .subtitle {
    position: absolute; left: 40px; top: 92px;
    color: var(--white); font-weight: 400; font-size: 20px; letter-spacing: 0.5px;
  }
  .intro {
    position: absolute; left: 0; top: 242px; width: 680px;
    text-align: center; color: var(--ink-blue);
    font-size: 14px; font-weight: 500; line-height: 24px; letter-spacing: 0.3px;
  }
  .offer {
    position: absolute; left: 0; top: 320px; width: 680px;
    text-align: center; color: var(--ink-blue);
    font-size: 17px; font-weight: 700; letter-spacing: 0.3px;
  }
  .service-tile {
    position: absolute; width: 148px; height: 138px;
    background: var(--tile-blue);
    display: flex; flex-direction: column; align-items: center; justify-content: flex-end;
    padding-bottom: 20px;
  }
  .service-icon {
    width: 62px; height: 58px; margin-bottom: 14px;
    border-radius: 4px;
    background: rgba(255,255,255,0.22);
  }
  .service-label {
    color: var(--white); font-weight: 700; font-size: 9.5px; letter-spacing: 0.2px;
    text-align: center; white-space: nowrap;
  }
  .tile-residential { left: 36px;  top: 410px; }
  .tile-commercial  { left: 266px; top: 410px; }
  .tile-landscaping { left: 496px; top: 410px; }
  .tile-concrete    { left: 154px; top: 598px; }
  .tile-painting    { left: 378px; top: 598px; }
  .footer {
    position: absolute; left: 0; top: 852px; width: 680px; height: 83px;
    background: var(--brand-blue); color: var(--white);
  }
  .brand-name {
    position: absolute; left: 26px; top: 29px;
    font-weight: 700; font-size: 18px; letter-spacing: 1px;
  }
  .office-line {
    position: absolute; left: 150px; top: 21px;
    font-size: 13px; font-weight: 400; white-space: nowrap;
  }
  .office-line strong { font-weight: 700; }
  .footer-rule {
    position: absolute; left: 150px; top: 43px; width: 480px; height: 1px;
    background: rgba(255,255,255,0.7);
  }
  .web-line {
    position: absolute; left: 150px; top: 51px;
    font-size: 11px; font-weight: 400; letter-spacing: 0.3px; white-space: nowrap;
  }
  .web-line strong { font-weight: 700; }
  .sep { margin: 0 6px; }
</style>
</head>
<body>
  <main class="flyer">
    <div class="backdrop-photo" role="img" aria-label="Glass skyscraper viewed from below with a tower crane, washed out"></div>
    <div class="header-photo" role="img" aria-label="Red hard hat resting on a ledge at a construction site"></div>
    <svg class="header-panel" width="680" height="170" viewBox="0 0 680 170" aria-hidden="true">
      <polygon points="0,0 335,0 420,170 0,170" fill="var(--brand-blue)"/>
    </svg>
    <h1 class="title">CONSTRUCTION</h1>
    <div class="title-rule"></div>
    <p class="subtitle">SERVICES</p>

    <p class="intro">AS A NEW TENANTS TO THE BUILDING AND AS A WAY<br>OF INTRODUCING OURSELVES WE WOULD LIKE TO OFFER</p>
    <p class="offer">A 10% DISCOUNT ON ANY &nbsp;OF THE BELOW SERVICES</p>

    <div class="service-tile tile-residential">
      <div class="service-icon" role="img" aria-label="House icon"></div>
      <span class="service-label">RESIDENTIAL BUILDING</span>
    </div>
    <div class="service-tile tile-commercial">
      <div class="service-icon" role="img" aria-label="Office towers icon"></div>
      <span class="service-label">COMMERCIAL BUILDING</span>
    </div>
    <div class="service-tile tile-landscaping">
      <div class="service-icon" role="img" aria-label="Trees and hills icon"></div>
      <span class="service-label">LANDSCAPING</span>
    </div>
    <div class="service-tile tile-concrete">
      <div class="service-icon" role="img" aria-label="Concrete mixer truck icon"></div>
      <span class="service-label">CONCRETE</span>
    </div>
    <div class="service-tile tile-painting">
      <div class="service-icon" role="img" aria-label="Paint roller icon"></div>
      <span class="service-label">PAINTING</span>
    </div>

    <footer class="footer">
      <span class="brand-name">CORVANE</span>
      <p class="office-line"><strong>HOME OFFICE:</strong> 1300 22 4810 . &nbsp;Suite 2.04 , 18 Harbour Lane Westmead</p>
      <div class="footer-rule"></div>
      <p class="web-line"><strong>WWW.CORVANE-SERVICES.COM.AU</strong>&nbsp; SYDNEY<span class="sep">|</span>CANBERRA<span class="sep">|</span>BRISBANE<span class="sep">|</span>MELBOURNE</p>
    </footer>
  </main>
</body>
</html>
```